Business cards for law firm with global theme

I'd like business cards with contact info for two offices. They should include the colors and font of the new logo design, which is a stylized globe with an "F" in it. The feel should be very modern and professional.

```html
<!DOCTYPE html>
<html lang="en">
<head>
<meta charset="utf-8">
<title>Valcourt Law – Business Cards</title>
<link rel="stylesheet" href="https://fonts.googleapis.com/css2?family=Source+Sans+3:wght@400;600;700&display=swap">
<style>
  :root {
    --backdrop: #e4e5e6;
    --navy: #133e6e;
    --navy-deep: #0c2c55;
    --navy-soft: #4d72a8;
    --sky: #2ba3dc;
    --paper: #f4f4f4;
    --ink: #1d3a63;
    --mist: #dde8ef;
    --mist-deep: #d3dde6;
  }
  * { margin: 0; padding: 0; box-sizing: border-box; }
  html, body {
    width: 1200px; height: 960px; overflow: hidden;
    background: var(--backdrop);
    font-family: "Source Sans 3", "Source Sans Pro", Arial, sans-serif;
  }
  .canvas { position: relative; width: 1200px; height: 960px; }

  .card { position: absolute; left: 294px; width: 611px; height: 349px; overflow: hidden; }

  /* Front */
  .card--front { top: 103px; background: var(--navy); }
  .front-texture {
    position: absolute; inset: 0;
    background: linear-gradient(100deg, var(--navy-soft) 0%, #2c528a 35%, #143d6c 65%, var(--navy-deep) 100%);
  }
  .front-brand {
    position: absolute; left: 87px; top: 212px;
    display: flex; align-items: center; gap: 14px;
  }
  .brand-dot { width: 60px; height: 60px; border-radius: 50%; background: var(--sky); }
  .front-brand .brand-name {
    color: #ffffff; font-weight: 700; font-size: 27px; letter-spacing: 0.5px; line-height: 1;
  }

  /* Back */
  .card--back { top: 505px; background: var(--paper); }
  .back-stripe { position: absolute; left: 0; top: 0; width: 16px; height: 100%; background: var(--navy); }
  .back-stripe-accent { position: absolute; left: 0; bottom: 0; width: 16px; height: 92px; background: var(--sky); }
  .back-decoration {
    position: absolute; left: 292px; top: 0; width: 319px; height: 349px;
    background: radial-gradient(ellipse at 60% 55%, var(--mist-deep) 0%, var(--mist) 55%, rgba(221,232,239,0) 100%);
  }
  .back-brand { position: absolute; left: 54px; top: 40px; display: flex; flex-direction: column; align-items: center; width: 194px; }
  .back-brand .brand-dot { width: 76px; height: 76px; margin-bottom: 18px; }
  .back-brand .brand-name { color: var(--navy); font-weight: 700; font-size: 32px; letter-spacing: 0.5px; line-height: 1; }

  .person { position: absolute; left: 54px; top: 266px; }
  .person-name { color: var(--sky); font-weight: 700; font-size: 21px; line-height: 1.2; }
  .person-title { color: var(--ink); font-size: 16px; line-height: 1.3; }

  .contact { position: absolute; left: 364px; top: 145px; color: var(--ink); font-size: 16px; line-height: 21px; }
  .office { margin-bottom: 9px; }
  .contact-list { list-style: none; margin-top: 13px; }
  .contact-list li { display: flex; align-items: center; gap: 6px; }
  .contact-list svg { width: 14px; height: 14px; flex: none; }
</style>
</head>
<body>
<div class="canvas">

  <section class="card card--front" aria-label="Card front">
    <div class="front-texture" role="img" aria-label="Repeating brand pattern fading from light to dark blue"></div>
    <div class="front-brand">
      <span class="brand-dot"></span>
      <span class="brand-name">VALCOURT LAW</span>
    </div>
  </section>

  <section class="card card--back" aria-label="Card back">
    <div class="back-stripe"></div>
    <div class="back-stripe-accent"></div>
    <div class="back-decoration" role="img" aria-label="Large faint brand emblem watermark"></div>

    <div class="back-brand">
      <span class="brand-dot"></span>
      <span class="brand-name">VALCOURT LAW</span>
    </div>

    <div class="person">
      <p class="person-name">Daniel Reyes</p>
      <p class="person-title">Attorney at Law</p>
    </div>

    <address class="contact" style="font-style:normal">
      <p class="office">38 Mercer St. Ste. 210<br>NYC, NY 10012</p>
      <p class="office">92 Greene St. Ste. 405<br>NYC, NY 10012</p>
      <ul class="contact-list">
        <li>
          <svg viewBox="0 0 16 16" aria-hidden="true"><path d="M4 1.5l2.2 3-1.3 1.6c.8 1.8 2.2 3.2 4 4l1.6-1.3 3 2.2-1 2.5C7 13.4 2.6 9 1.5 3.5z" fill="none" stroke="#1d3a63" stroke-width="1.4" stroke-linejoin="round"/></svg>
          (212) 555-0148
        </li>
        <li>
          <svg viewBox="0 0 16 16" aria-hidden="true"><rect x="1.5" y="3.5" width="13" height="9" fill="none" stroke="#1d3a63" stroke-width="1.4"/><path d="M1.5 3.5L8 9l6.5-5.5" fill="none" stroke="#1d3a63" stroke-width="1.4"/></svg>
          daniel@valcourtlaw.com
        </li>
        <li>
          <svg viewBox="0 0 16 16" aria-hidden="true"><circle cx="8" cy="8" r="6.3" fill="none" stroke="#1d3a63" stroke-width="1.3"/><ellipse cx="8" cy="8" rx="2.7" ry="6.3" fill="none" stroke="#1d3a63" stroke-width="1.1"/><path d="M1.7 8h12.6" stroke="#1d3a63" stroke-width="1.1"/></svg>
          www.valcourtlaw.com
        </li>
      </ul>
    </address>
  </section>

</div>
</body>
</html>
```